依頼詳細
メルマガ登録用のランディングページをお願いします。概要に書かせて頂いた通り、
変わるきっかけが欲しいけどなかなか行動できない方たちが、
作成していただいたLPから可能性を感じて、
ここなら変われるかも知れないと期待感が湧きでるような、
未来を想像して興奮してしまうような感じでお願いします。
ファーストインプレッションは大事にしたいです。

スマホとPCのどちらでも見られるような大きさでお願いします。
サイトURL
http://hanabira-tsumugi.com/lp/
ページ数
1ページ
希望イメージ
シンプル 複雑
単色 カラフル
暗い 明るい
日常 高級
遊び心 厳粛
未来的 伝統的
女性的 男性的
希望する色
納品ファイル
補足説明
作成していただいたLP内の文章などあとで、
wordpressで編集できるようにしていただきたいです。
初めての依頼なので、作成していただく時点で不明点などあれば、
すぐに追記させていただきます!!!
提案の締め切りを1日のばしました。
みなさまのご提案楽しみにしております。
■ 選んだ理由

ファーストインパクトが気に入りました。

■ 提案者全員のお礼・コメント

初心者の提案でも丁寧に提案していただきみなさまありがとうございます。

```html
<!DOCTYPE html>
<html lang="ja">
<head>
<meta charset="utf-8">
<title>モテない男の大逆転 | メルマガ登録</title>
<link rel="stylesheet" href="https://fonts.googleapis.com/css2?family=Noto+Sans+JP:wght@400;700;900&family=Noto+Serif+JP:wght@700;900&display=swap">
<style>
:root{
  --page-bg:#cdcdcd;
  --column-bg:#f3f3f3;
  --navy:#1b2d63;
  --royal:#1f4fa8;
  --red:#d4121d;
  --deep-red:#a50a12;
  --orange:#f08a17;
  --yellow:#f6d04a;
  --ink:#1f1f1f;
  --white:#ffffff;
  --panel:#e4e4e4;
  --brown:#5b3a24;
  --sky:#cfe2f5;
}
*{box-sizing:border-box;margin:0;padding:0}
html,body{width:1200px;height:5068px;overflow:hidden}
body{background:var(--page-bg);font-family:"Noto Sans JP",sans-serif;color:var(--ink);position:relative}
.column{position:absolute;left:200px;top:0;width:800px;height:5020px;background:var(--column-bg)}
.abs{position:absolute}

/* hero */
.hero{left:0;top:0;width:800px;height:440px;background:linear-gradient(100deg,var(--navy) 0%,#3d5790 38%,#d9dde6 62%,#eef0f4 100%)}
.hero-title{left:24px;top:14px;color:var(--white);font-size:42px;font-weight:900;letter-spacing:2px;white-space:nowrap}
.hero-photo{left:300px;top:60px;width:380px;height:380px;background:linear-gradient(180deg,#cfcfd6,#8c8c98)}
.badge{left:660px;top:24px;width:120px;height:120px;border-radius:50%;background:radial-gradient(circle,#f4d77a,#b88a1f);border:4px solid #fff3c4}
.hero-banner{left:20px;top:430px;width:760px;height:76px;background:var(--red);color:var(--white);font-size:34px;font-weight:900;display:flex;align-items:center;justify-content:center;transform:skewY(-2deg);white-space:nowrap}
.hero-lead{left:20px;top:528px;width:760px;text-align:center;font-size:33px;font-weight:900;line-height:1.45}
.hero-lead em{font-style:normal;color:var(--red);font-size:46px}

/* ribbon */
.ribbon{left:30px;width:740px;height:100px}
.ribbon-text{position:absolute;left:0;top:0;width:100%;height:100%;display:flex;align-items:center;justify-content:center;color:var(--white);font-size:30px;font-weight:700;transform:rotate(-3deg);white-space:nowrap}

/* form */
.signup{left:30px;width:740px;background:var(--panel);border-radius:14px;border:2px solid #bdbdbd;padding:22px 34px}
.field{display:flex;align-items:center;margin-bottom:12px}
.field-label{width:190px;font-size:21px;font-weight:700;white-space:nowrap}
.field-input{flex:1;height:40px;background:var(--white);border:1px solid #aaa}
.signup-button{margin:8px auto 0;width:560px;height:56px;border-radius:8px;background:linear-gradient(#f9a33a,#e06d06);color:var(--white);font-size:24px;font-weight:700;display:flex;align-items:center;justify-content:center;gap:14px}

/* headings */
.chevron-heading{left:0;width:800px;height:130px}
.chevron-heading span{position:absolute;left:0;top:12px;width:100%;text-align:center;color:var(--white);font-size:40px;font-weight:900;letter-spacing:2px;white-space:nowrap}

/* checklist */
.checklist{left:30px;top:1120px;width:740px;height:580px;background:var(--yellow);padding:30px 40px;list-style:none}
.checklist li{display:flex;align-items:center;gap:14px;height:52px;font-size:22px;font-weight:700;border-bottom:1px dashed #a88a1a;white-space:nowrap}
.checkbox{width:26px;height:26px;border:3px solid var(--ink);background:var(--white);flex:none}

/* mind section */
.mind{left:0;top:1720px;width:800px;height:520px;background:repeating-linear-gradient(45deg,#3a3a3a 0 10px,#444 10px 20px)}
.mind-heading{left:30px;top:20px;width:740px;height:70px;background:linear-gradient(90deg,#222 0 60px,var(--red) 60px);color:var(--white);font-size:30px;font-weight:900;display:flex;align-items:center;padding-left:90px;white-space:nowrap}
.mind-card{left:30px;top:110px;width:740px;height:380px;background:var(--white);padding:24px}
.mind-photo{left:24px;top:24px;width:270px;height:230px;background:linear-gradient(#e8e8e8,#a0a0a8)}
.mind-copy{left:320px;top:24px;width:396px;font-size:17px;line-height:1.75}
.mind-copy strong{color:var(--red)}

.goal-band{left:0;top:2250px;width:800px;height:120px;background:linear-gradient(90deg,#0e4a9b,#2d78d0);transform:skewY(-2deg);display:flex;flex-direction:column;align-items:center;justify-content:center;color:#ff5c7a;font-size:30px;font-weight:900;line-height:1.35}

.orange-heading{left:30px;top:2400px;width:740px;height:76px;background:linear-gradient(#f8b03a,var(--orange));font-size:34px;font-weight:900;color:var(--deep-red);display:flex;align-items:center;justify-content:center;white-space:nowrap}
.orange-heading span{color:var(--navy)}
.worries{left:30px;top:2490px;width:740px;height:370px;background:linear-gradient(#d8d8d8,#ededed)}
.worry-figure{left:330px;top:14px;width:80px;height:110px;background:linear-gradient(#777,#333)}
.cloud{fill:var(--navy)}
.cloud-label{font-family:"Noto Sans JP",sans-serif;font-size:22px;font-weight:700;fill:var(--white);text-anchor:middle}
.cloud-label.accent{fill:#ffe14d}
.core-label{font-family:"Noto Sans JP",sans-serif;font-size:22px;font-weight:900;fill:var(--red);text-anchor:middle}

/* practice grid */
.practice{left:30px;top:3080px;width:740px;height:1020px;border:6px solid var(--navy);background:var(--sky);padding:30px}
.topic-label{position:absolute;width:280px;height:66px;background:var(--deep-red);border:3px solid #fff;color:var(--white);font-size:28px;font-weight:700;display:flex;align-items:center;justify-content:center}
.topic-art{position:absolute;width:180px;height:130px}
.technique-bar{left:80px;top:890px;width:568px;height:76px;background:var(--royal);color:var(--white);font-size:32px;font-weight:900;display:flex;align-items:center;justify-content:center;letter-spacing:3px}

/* invitation */
.invite{left:30px;top:4120px;width:740px;height:340px;background:var(--brown);padding:24px}
.invite-inner{width:100%;height:100%;background:linear-gradient(#7a5640,#5e3f2b);display:flex;flex-direction:column;align-items:center;justify-content:center;font-family:"Noto Serif JP",serif;color:var(--white);font-size:24px;font-weight:700;line-height:1.7;text-align:center}
.invite-inner .hl{color:#ff6b7f}
.invite-inner .free{display:inline-block;background:var(--white);color:var(--red);font-size:32px;font-weight:900;padding:0 20px;margin:4px 0}

.notes{left:0;top:4830px;width:800px;text-align:center;font-size:16px;line-height:2}
.notes a{color:var(--royal);text-decoration:underline}
.footer{left:0;top:5020px;width:1200px;height:48px;background:#222;color:#ddd;font-size:15px;display:flex;align-items:center;justify-content:center}
</style>
</head>
<body>
<main class="column">

  <header>
    <div class="abs hero"></div>
    <div class="abs hero-photo" role="img" aria-label="笑顔で寄り添うスーツ姿の男性と女性の写真"></div>
    <h1 class="abs hero-title">モテない男の大逆転</h1>
    <div class="abs badge" role="img" aria-label="金色の円形バッジ"></div>
    <p class="abs hero-banner">モテない人生から180°人生を変えてみませんか！</p>
    <p class="abs hero-lead">たった<em>1</em>カ月で美女揃いの5人の女性を<br>虜にする方法を伝授します！！</p>
  </header>

  <section>
    <div class="abs ribbon" style="top:640px">
      <svg width="740" height="100" viewBox="0 0 740 100"><polygon points="0,40 50,30 40,60 60,95 10,90" fill="#0d2f7a"/><polygon points="690,10 740,20 720,45 740,70 690,62" fill="#0d2f7a"/><polygon points="30,30 710,0 715,62 35,92" fill="var(--royal)"/></svg>
      <p class="ribbon-text">あなたも今すぐ、こちらからメルマガ登録どうぞ</p>
    </div>
    <form class="abs signup" style="top:752px;height:188px">
      <div class="field"><span class="field-label">お名前</span><span class="field-input"></span></div>
      <div class="field"><span class="field-label">メールアドレス</span><span class="field-input"></span></div>
      <div class="signup-button">今すぐ、無料でメルマガ登録する <span>▶</span></div>
    </form>
  </section>

  <section>
    <div class="abs chevron-heading" style="top:960px">
      <svg width="800" height="130" viewBox="0 0 800 130"><polygon points="0,0 800,0 800,70 400,130 0,70" fill="var(--red)"/></svg>
      <span>こんな方におすすめです</span>
    </div>
    <ul class="abs checklist">
      <li><span class="checkbox"></span>自分に自信がなく自分自身を変えたい人</li>
      <li><span class="checkbox"></span>一緒に恋愛活動を頑張っていける仲間が欲しい人</li>
      <li><span class="checkbox"></span>女性とのいろいろな場所で出会う方法を知りたい人</li>
      <li><span class="checkbox"></span>出会った女性と一瞬で仲良くなれる方法を知りたい人</li>
      <li><span class="checkbox"></span>友達から恋人に発展する方法を知りたい人</li>
      <li><span class="checkbox"></span>自分に合ったやり方を知りたい人</li>
      <li><span class="checkbox"></span>恋人までいけず、いい人止まりで終わってしまう人</li>
      <li><span class="checkbox"></span>タイプ別の落とし方を知りたい人</li>
      <li><span class="checkbox"></span>モチベーションが上がらず、すぐに諦めてしまう人</li>
      <li><span class="checkbox"></span>本当に効果があるのかわからないし信用できない人</li>
    </ul>
  </section>

  <section class="abs mind">
    <h2 class="abs mind-heading">恋愛テクニックよりも重要な恋愛マインド</h2>
    <div class="abs mind-card">
      <div class="abs mind-photo" role="img" aria-label="頭を抱えて座り込むスーツ姿の男性の写真"></div>
      <p class="abs mind-copy">あなたは女性からの視線、容姿を恐れどんどんと自分の殻に閉じこもってしまっていませんか。自分の殻に閉じこもるあまりいつの間にか女性に対して恐怖心を抱き、一歩が踏み出せなくなっているのです。まずはその<strong>心の壁を取り除く</strong>ことから始めていくプログラムを用意しています。メール講座を通じてその方法をお伝えします。</p>
    </div>
  </section>

  <p class="abs goal-band"><span>恋愛の考え方の重要性を理解している</span><span>真のモテ男を目指そう</span></p>

  <section>
    <h2 class="abs orange-heading">思春期<span>の苦い記憶、過去からの脱却</span></h2>
    <div class="abs worries">
      <svg width="740" height="370" viewBox="0 0 740 370">
        <ellipse class="cloud" cx="170" cy="130" rx="130" ry="62"/>
        <ellipse class="cloud" cx="580" cy="110" rx="120" ry="60"/>
        <ellipse class="cloud" cx="200" cy="270" rx="120" ry="62"/>
        <ellipse class="cloud" cx="540" cy="270" rx="125" ry="62"/>
        <ellipse cx="370" cy="190" rx="120" ry="55" fill="#2a3f80"/>
        <text class="cloud-label" x="170" y="138">恥ずかしがり屋</text>
        <text class="cloud-label accent" x="580" y="118">口下手</text>
        <text class="cloud-label" x="200" y="278">人見知り</text>
        <text class="cloud-label accent" x="540" y="278">会話が苦手</text>
        <text class="core-label" x="370" y="198">劣等感が強くなる</text>
      </svg>
      <div class="abs worry-figure" role="img" aria-label="うつむいて立つ男性のシルエット"></div>
    </div>
  </section>

  <section>
    <div class="abs chevron-heading" style="top:2920px">
      <svg width="800" height="130" viewBox="0 0 800 130"><polygon points="0,0 800,0 800,70 400,130 0,70" fill="var(--red)"/></svg>
      <span>女性に対する接し方を学びながら実践</span>
    </div>
    <div class="abs practice">
      <div class="topic-label" style="left:40px;top:30px">恋愛本</div>
      <div class="topic-label" style="left:408px;top:30px">ナンパ</div>
      <div class="topic-art" role="img" aria-label="ピンク色の本" style="left:90px;top:110px;background:#f3a6c4"></div>
      <div class="topic-art" role="img" aria-label="歩く男女のシルエット" style="left:460px;top:110px;background:linear-gradient(#5f8fd6,#2f5fae)"></div>
      <div class="topic-label" style="left:40px;top:270px">自己啓発本</div>
      <div class="topic-label" style="left:408px;top:270px">口説き</div>
      <div class="topic-art" role="img" aria-label="積み重ねた本" style="left:90px;top:350px;background:linear-gradient(#6a6a6a,#2a2a2a)"></div>
      <div class="topic-art" role="img" aria-label="向かい合って座る男女のシルエット" style="left:460px;top:350px;background:linear-gradient(#e27ac4,#b03d8f)"></div>
      <div class="topic-label" style="left:40px;top:510px">女性心理</div>
      <div class="topic-label" style="left:408px;top:510px">交渉術</div>
      <div class="topic-art" role="img" aria-label="考え込む女性の写真" style="left:90px;top:590px;height:200px;background:linear-gradient(#f1e3d6,#c9a98e)"></div>
      <div class="topic-art" role="img" aria-label="握手するビジネスマンのシルエット" style="left:460px;top:590px;height:200px;background:linear-gradient(#3a3a3a,#111)"></div>
      <div class="abs technique-bar" style="top:840px">誘導テクニック</div>
    </div>
  </section>

  <section class="abs invite">
    <div class="invite-inner">
      <p>現在モテない男でも、内向性が高くても<br>これまで学んだ<span class="hl">恋愛マインド</span>を</p>
      <p class="free">完全無料で</p>
      <p>あなたに自信を持つ方法をお伝えします<br><span class="hl">本気</span>の人のみ参加してください。</p>
    </div>
  </section>

  <section>
    <div class="abs ribbon" style="top:4500px">
      <svg width="740" height="100" viewBox="0 0 740 100"><polygon points="0,40 50,30 40,60 60,95 10,90" fill="#0d2f7a"/><polygon points="690,10 740,20 720,45 740,70 690,62" fill="#0d2f7a"/><polygon points="30,30 710,0 715,62 35,92" fill="var(--royal)"/></svg>
      <p class="ribbon-text">今ならキャンペーンに付き豪華プレゼント！！</p>
    </div>
    <form class="abs signup" style="top:4612px;height:200px">
      <div class="field"><span class="field-label">お名前</span><span class="field-input"></span></div>
      <div class="field"><span class="field-label">メールアドレス</span><span class="field-input"></span></div>
      <div class="signup-button">今すぐ、無料で登録する <span>▶</span></div>
    </form>
    <div class="abs notes">
      <p>※ご入力頂いた情報は個人情報保護法に基づいて厳重に管理致します。</p>
      <p>安心してご記入下さい。</p>
      <p>プライバシーポリシーはこちらです。</p>
      <p><a>特定商取引法の表記</a> ｜ <a>プライバシーポリシー</a></p>
    </div>
  </section>
</main>
<footer class="abs footer">Copyright (C) 2016 Tsumugi Works Inc. All Rights Reserved.</footer>
</body>
</html>
```